Vorla constructions

We are predominantly a residential home builder based in Melbourne, Victoria Australia. We construct houses, apartments, townhouses, multi-unit developments.

The name of the company is "Vorla Constructions"
My company believes in building unique construction projects mainly residential homes. The target customers are upmarket Melbourne residents/investors.

I want the brand name "Vorla" to be part of the logo. There's no need to put the word construction in the logo at this stage.

I would also like some ideas for a slogan e.g. "Just build it." or "We build quality homes." But I would like something unique and different for a slogan not the same old cliche.

vorlaconstructions-example.com.au
e: mdelton@vorlaconstructions-example.com.au
M: 0417836519
Address: 8/3 Marlow Close Clayton VIC 3168

Director:Mr Desmond Kellingworth

```html
<!DOCTYPE html>
<html lang="en">
<head>
<meta charset="utf-8">
<title>Vorla Constructions – Business Card</title>
<link href="https://fonts.googleapis.com/css2?family=Arimo:wght@400;700&family=Poiret+One&family=Yanone+Kaffeesatz:wght@300&display=swap" rel="stylesheet">
<style>
  :root {
    --stage: #2b2b2b;
    --orange: #f0821f;
    --grey: #b9b8b9;
    --blue: #1eaee4;
    --white: #ffffff;
    --ink: #2a2420;
    --faint-tan: rgba(150, 170, 150, 0.45);
    --faint-blue: rgba(120, 185, 215, 0.55);
  }
  * { margin: 0; padding: 0; box-sizing: border-box; }
  html, body {
    width: 1200px; height: 1200px; overflow: hidden;
    background: var(--stage);
  }
  .card {
    position: absolute; left: 150px; width: 900px; height: 515px;
    overflow: hidden;
    box-shadow: 0 18px 40px rgba(0,0,0,0.55);
  }
  .card--front { top: 55px; background: var(--orange); }
  .card--back { top: 630px; background: var(--grey); }

  .front__mark-area {
    position: absolute; left: -170px; top: 90px;
    width: 460px; height: 460px; border-radius: 50%;
    background: var(--faint-tan);
  }
  .brand {
    position: absolute;
    font-family: "Arimo", sans-serif; font-weight: 700;
    color: var(--blue); letter-spacing: 2px; line-height: 1;
  }
  .front__brand { left: 380px; top: 150px; font-size: 110px; }
  .front__descriptor {
    position: absolute; left: 470px; top: 272px;
    font-family: "Poiret One", sans-serif; font-size: 30px;
    letter-spacing: 14px; color: var(--white);
  }
  .front__tagline {
    position: absolute; left: 400px; top: 325px;
    font-family: "Yanone Kaffeesatz", sans-serif; font-weight: 300;
    font-size: 40px; color: var(--ink);
  }

  .back__band { position: absolute; inset: 0; }
  .back__mark-area {
    position: absolute; right: 70px; top: -60px;
    width: 260px; height: 260px; border-radius: 50%;
    background: var(--faint-blue);
  }
  .back__brand { left: 100px; top: 160px; font-size: 64px; }
  .back__descriptor {
    position: absolute; left: 104px; top: 235px;
    font-family: "Poiret One", sans-serif; font-size: 24px;
    letter-spacing: 9px; color: var(--white);
  }
  .contact {
    position: absolute; left: 330px; top: 335px;
    list-style: none;
    font-family: "Arimo", sans-serif; color: var(--white);
  }
  .contact__item { display: flex; align-items: flex-start; gap: 22px; margin-bottom: 12px; }
  .contact__icon { width: 30px; height: 26px; flex: none; margin-top: 2px; }
  .contact__text { font-size: 19px; line-height: 1.3; }
  .contact__text--phone { font-size: 24px; }
</style>
</head>
<body>

<section class="card card--front" aria-label="Card front">
  <div class="front__mark-area" role="img" aria-label="Faint brand emblem decoration"></div>
  <div class="brand front__brand">Vorla</div>
  <div class="front__descriptor">residential</div>
  <div class="front__tagline">Qulity House For an Qulity Life</div>
</section>

<section class="card card--back" aria-label="Card back">
  <div class="back__mark-area" role="img" aria-label="Faint brand emblem decoration"></div>
  <svg class="back__band" viewBox="0 0 900 515" preserveAspectRatio="none" aria-hidden="true">
    <polygon points="0,318 900,268 900,515 0,515" fill="var(--orange)"/>
    <polygon points="0,310 900,260 900,269 0,319" fill="var(--white)"/>
  </svg>
  <div class="brand back__brand">Vorla</div>
  <div class="back__descriptor">construction</div>

  <ul class="contact">
    <li class="contact__item">
      <svg class="contact__icon" viewBox="0 0 30 26" aria-hidden="true">
        <path d="M3 12 L15 3 L27 12" fill="none" stroke="#fff" stroke-width="2"/>
        <rect x="6" y="11" width="18" height="13" fill="none" stroke="#fff" stroke-width="2"/>
        <rect x="12" y="16" width="6" height="8" fill="#fff"/>
      </svg>
      <span class="contact__text">8/3 Marlow Close Tarrowby KV 9041</span>
    </li>
    <li class="contact__item">
      <svg class="contact__icon" viewBox="0 0 30 26" aria-hidden="true">
        <rect x="2" y="5" width="26" height="17" fill="none" stroke="#fff" stroke-width="2"/>
        <path d="M2 5 L15 15 L28 5" fill="none" stroke="#fff" stroke-width="2"/>
      </svg>
      <span class="contact__text">mdelton@vorlaconstructions-example.com.au<br>vorlaconstructions-example.com.au</span>
    </li>
    <li class="contact__item">
      <svg class="contact__icon" viewBox="0 0 30 26" aria-hidden="true">
        <rect x="2" y="0" width="26" height="26" rx="5" fill="#fff"/>
        <path d="M10 5 L13 9 L11 11 C12 14 14 16 17 17 L19 15 L23 18 L21 21 C14 21 8 15 8 7 Z" fill="var(--orange)"/>
      </svg>
      <span class="contact__text contact__text--phone">0417836519</span>
    </li>
  </ul>
</section>

</body>
</html>
```